Flyer Erste-Hilfe-Kurse für Kinder
Zielgruppe
Wir sind eine private Firma und bieten verschiedene Erste-Hilfe-Kurse an.
Liebe Designer,
wir, die märkische Helferakademie, wollen uns im Bereich der Erste-Hilfe-Kurse für Kinder im Alter zwischen 6 bis 14 Jahre etablieren und wünschen uns daher einen passenden Flyer.
Folgende Sachen sind uns dabei besonders wichtig:
Märkische Helferakademie
Lindauer Weg 4
21079 Hamburg
Tel.: 040 71 84 29 03
Website: www.maerkische-helferakademie.de
In diesen Kursen lernen Kinder auf spielerische Art und Weise, Notfälle zu erkennen, sich zu organisieren und selbstständig Erste Hilfe zu leisten, auf Eigenschutz zu achten und einen Notruf abgeben zu können.
Weitere mögliche Themen sind: Auffinden einer bewusstlosen Person, Reanimation und Verbände.
Der Flyer soll farbenfroh gestaltet werden und darf gerne Bilder beinhalten.
Um einen Überblick über unsere Firma zu bekommen, kann man sich gerne unsere Website anschauen.
Der Flyer soll eine Vorder- und Rückseite haben.
Unser Logo kann für die Gestaltung von der Website genutzt werden und nach Auswahl des Gewinners von uns als Datei gerne bereitgestellt werden.
Wir freuen uns über Vorschläge.

```html
<!DOCTYPE html>
<html lang="de">
<head>
<meta charset="utf-8">
<title>Flyer Erste-Hilfe-Kurse für Kinder</title>
<link rel="stylesheet" href="https://fonts.googleapis.com/css2?family=Bangers&family=Arimo:wght@400;700&display=swap">
<style>
  :root {
    --stage: #a8383a;
    --yellow: #fcbd00;
    --orange: #fb7410;
    --red: #e3221d;
    --deep-red: #c0110f;
    --ink: #161616;
    --white: #ffffff;
  }
  * { box-sizing: border-box; margin: 0; padding: 0; }
  html, body { width: 1200px; height: 675px; overflow: hidden; }
  body { background: var(--stage); font-family: "Arimo", Arial, sans-serif; color: var(--ink); position: relative; }

  .page {
    position: absolute; top: 59px; width: 392px; height: 556px;
    background: var(--yellow); overflow: hidden;
    box-shadow: 0 10px 24px rgba(0,0,0,.35);
  }
  .page--front { left: 178px; }
  .page--back { left: 628px; }

  .page svg.decor { position: absolute; inset: 0; width: 100%; height: 100%; }

  .comic { font-family: "Bangers", "Impact", sans-serif; font-weight: 400; letter-spacing: .3px; }

  /* front */
  .headline { position: absolute; left: 50px; top: 62px; width: 260px; height: 120px; transform: rotate(-5deg); transform-origin: left top; line-height: 1; }
  .headline__main { position: absolute; left: 0; top: 0; color: var(--deep-red); font-size: 34px; white-space: nowrap; }
  .headline__big { position: absolute; left: 86px; top: 34px; color: var(--deep-red); font-size: 33px; white-space: nowrap; }
  .headline__kicker { position: absolute; left: 12px; top: 44px; font-size: 11px; line-height: 1.2; color: var(--ink); white-space: nowrap; }
  .headline__kicker span { display: block; padding-left: 18px; }
  .headline__sub { position: absolute; left: 16px; top: 78px; font-size: 11px; color: var(--ink); white-space: nowrap; }

  .illustration {
    position: absolute; left: 10px; top: 175px; width: 372px; height: 345px;
    border-radius: 120px 120px 10px 10px;
    background: radial-gradient(ellipse at 40% 35%, #f7d2b8 0%, #f0b9c4 30%, #4aa3c7 62%, rgba(252,189,0,0) 80%);
  }

  .brand { position: absolute; display: flex; align-items: flex-start; gap: 6px; }
  .brand__dot { width: 14px; height: 14px; border-radius: 50%; background: var(--red); margin-top: 2px; flex: none; }
  .brand__name { font-size: 16px; line-height: 19px; font-weight: 400; color: var(--ink); white-space: nowrap; }
  .brand__tag { font-size: 7.6px; line-height: 10px; color: var(--ink); margin-top: 2px; padding-left: 14px; white-space: nowrap; }
  .page--front .brand { left: 148px; top: 508px; }

  /* back */
  .side-head { position: absolute; left: 34px; color: var(--white); font-size: 23px; line-height: 28px; transform: skewX(-4deg); }
  .copy { position: absolute; left: 180px; font-size: 9.2px; line-height: 14px; color: var(--ink); }
  .copy--intro { width: 162px; top: 34px; }
  .checklist { width: 196px; list-style: none; }
  .checklist li { position: relative; padding-left: 11px; }
  .checklist li::before {
    content: ""; position: absolute; left: 0; top: 4px; width: 6px; height: 6px;
    background:
      linear-gradient(var(--red), var(--red)) center/6px 2px no-repeat,
      linear-gradient(var(--red), var(--red)) center/2px 6px no-repeat;
  }
  .cta { position: absolute; left: 22px; top: 484px; transform: rotate(-6deg); line-height: 1.05; }
  .cta__main { color: var(--deep-red); font-size: 15px; }
  .cta__sub { font-size: 8px; color: var(--ink); }
  .page--back .brand { left: 186px; top: 486px; }
  .page--back .brand__name { font-size: 13px; line-height: 16px; }
  .page--back .brand__tag { font-size: 6.2px; line-height: 8px; margin-top: 1px; padding-left: 8px; }
  .contact { position: absolute; left: 214px; top: 516px; font-size: 7px; line-height: 10.5px; color: var(--ink); white-space: nowrap; }
  .contact strong { font-weight: 700; }
</style>
</head>
<body>

<section class="page page--front" aria-label="Vorderseite">
  <svg class="decor" viewBox="0 0 392 556" aria-hidden="true">
    <circle cx="392" cy="40" r="75" fill="var(--orange)"/>
    <path d="M0 400 L40 470 L70 556 L0 556Z M392 390 L360 470 L340 556 L392 556Z" fill="var(--red)"/>
    <g fill="var(--white)" opacity=".85">
      <path d="M346 100h4v7h7v4h-7v7h-4v-7h-7v-4h7z"/>
      <path d="M24 205h4v7h7v4h-7v7h-4v-7h-7v-4h7z"/>
      <path d="M352 300h4v7h7v4h-7v7h-4v-7h-7v-4h7z"/>
    </g>
  </svg>
  <div class="illustration" role="img" aria-label="Comic-Illustration: Mädchen und Junge mit weißen Kappen mit rotem Kreuz, Rucksäcken und Büchern"></div>
  <svg class="decor" viewBox="0 0 392 556" aria-hidden="true">
    <path d="M20 70 L55 55 L40 40 L120 45 L150 25 L200 40 L270 20 L300 35 L340 15 L325 60 L345 90 L318 110 L345 140 L300 150 L310 175 L250 165 L220 190 L190 170 L150 190 L120 175 L70 195 L85 160 L40 165 L55 135 L15 120 L45 100Z" fill="var(--white)" stroke="var(--ink)" stroke-width="3" stroke-linejoin="round"/>
    <path d="M110 556 L120 510 L95 500 L150 490 L190 505 L250 485 L310 500 L370 480 L355 520 L375 556Z" fill="var(--white)" stroke="var(--ink)" stroke-width="3" stroke-linejoin="round"/>
  </svg>

  <div class="headline comic">
    <div class="headline__main">KLEINE HELDEN –</div>
    <div class="headline__kicker">ERSTE HILFE<span>FÜR KINDER</span></div>
    <div class="headline__big">GROSSE HILFE</div>
    <div class="headline__sub">SPIELERISCH LERNEN, IM NOTFALL RICHTIG ZU HANDELN</div>
  </div>

  <div class="brand">
    <span class="brand__dot"></span>
    <div>
      <div class="brand__name">Märkische Helferakademie</div>
      <div class="brand__tag">Erste-Hilfe - Brandschutz - Infektionsschutz</div>
    </div>
  </div>
</section>

<section class="page page--back" aria-label="Rückseite">
  <svg class="decor" viewBox="0 0 392 556" aria-hidden="true">
    <circle cx="392" cy="40" r="75" fill="var(--orange)"/>
    <path d="M0 390 L60 470 L0 470Z" fill="var(--red)"/>
    <path d="M0 470 L150 470 L170 556 L0 556Z" fill="var(--red)"/>
    <path d="M8 505 L30 475 L20 455 L70 462 L110 445 L125 462 L150 452 L140 482 L160 505 L130 515 L135 540 L95 525 L60 545 L50 520 L12 528Z" fill="var(--white)" stroke="var(--ink)" stroke-width="2.5" stroke-linejoin="round"/>
    <path d="M150 556 L165 520 L155 470 L205 480 L250 460 L300 480 L350 458 L385 475 L375 520 L392 556Z" fill="var(--white)" stroke="var(--ink)" stroke-width="3" stroke-linejoin="round"/>
    <g fill="var(--white)" opacity=".85">
      <path d="M66 134h4v7h7v4h-7v7h-4v-7h-7v-4h7z"/>
      <path d="M350 100h4v7h7v4h-7v7h-4v-7h-7v-4h7z"/>
      <path d="M362 300h4v7h7v4h-7v7h-4v-7h-7v-4h7z"/>
    </g>
  </svg>

  <div class="side-head comic" style="top:36px">SICHER HANDELN.<br>MUTIG HELFEN.<br>LEBEN RETTEN.</div>
  <p class="copy copy--intro">In unseren speziell entwickelten Erste-Hilfe-Kursen für Kinder lernen junge Teilnehmer auf spielerische und altersgerechte Weise, wie sie Notfälle erkennen und richtig reagieren. Dabei stehen praktische Übungen, verständliche Erklärungen und realistische Situationen im Mittelpunkt – damit Kinder im Ernstfall ruhig und selbstständig handeln können.</p>

  <div class="side-head comic" style="top:198px">DAS LERNEN<br>KINDER IM KURS:</div>
  <ul class="copy checklist" style="top:198px">
    <li>Notfälle erkennen und richtig einschätzen</li>
    <li>Einen Notruf sicher absetzen</li>
    <li>Eigenschutz beachten („Ich helfe, ohne mich zu gefährden“)</li>
    <li>Verhalten bei bewusstlosen Personen</li>
    <li>Grundlagen der Wiederbelebung (Reanimation)</li>
    <li>Wunden versorgen und Verbände anlegen</li>
    <li>Teamarbeit und richtiges Verhalten in Stresssituationen</li>
  </ul>

  <div class="side-head comic" style="top:371px">WARUM<br>DIESER KURS?</div>
  <ul class="copy checklist" style="top:371px">
    <li>Spielerisches Lernen statt trockener Theorie</li>
    <li>Stärkung von Selbstbewusstsein und Verantwortungsgefühl</li>
    <li>Praxisnah durch erfahrene Ausbilder</li>
    <li>Vorbereitung auf reale Alltagssituationen</li>
  </ul>

  <div class="cta comic">
    <div class="cta__main">JETZT PLATZ SICHERN</div>
    <div class="cta__sub">UND ZUM LEBENSRETTER WERDEN!</div>
  </div>

  <div class="brand">
    <span class="brand__dot"></span>
    <div>
      <div class="brand__name">Märkische Helferakademie</div>
      <div class="brand__tag">Erste-Hilfe - Brandschutz - Infektionsschutz</div>
    </div>
  </div>
  <div class="contact">
    Lindauer Weg 4 · 21079 Hamburg<br>
    Tel. +49 40 71 84 29 03<br>
    <strong>www.maerkische-helferakademie.de</strong>
  </div>
</section>

</body>
</html>
```